Need a creative cover photo for social media profiles

We are rebranding and would like to promote the new look on our cover image for our social platforms (Pelmora, Quillane, Brindle). It should feel similar in brand as the attached collateral. We want this to make a statement as our new logo and feel are completely different from where we currently are. I am sending along examples of other collateral we have created.
Target Market(s)
IT, accounting professionals and companies looking to hire those professionals.
Industry/Entity Type
Staffing
Requirements
Must have
- Logo
Our corporate font is Nexa Bold for headlines and Ebrima for content.
CMYK combinations for our corporate colors
C 2. M 66, Y 87, K 0
C 84, M 69, Y 47, K 39

```html
<!DOCTYPE html>
<html lang="en">
<head>
<meta charset="utf-8">
<title>Corvane Group – Social Cover Set</title>
<link rel="stylesheet" href="https://fonts.googleapis.com/css2?family=Montserrat:wght@700;800&family=Noto+Sans:wght@400&display=swap">
<style>
  :root {
    --brand-orange: #ef8246;
    --brand-orange-deep: #ec7434;
    --brand-navy: #2c3f55;
    --brand-navy-fill: #34475c;
    --ring-white: #ffffff;
    --photo-light: #e6eef4;
    --photo-mid: #c7d4e0;
    --photo-warm: #d9c3ad;
    --text-light: #ffffff;
    --page: #ffffff;
  }
  * { margin: 0; padding: 0; box-sizing: border-box; }
  html, body {
    width: 1064px;
    height: 1200px;
    overflow: hidden;
    background: var(--page);
  }
  .cover-set {
    position: relative;
    width: 1064px;
    height: 1200px;
  }
  .cover {
    position: absolute;
    left: 42px;
    width: 982px;
    height: 362px;
    overflow: hidden;
  }
  .cover--orange-centre { top: 45px; }
  .cover--orange-right { top: 422px; }
  .cover--navy-centre { top: 800px; }

  .cover__photo {
    position: absolute;
    inset: 0;
    background:
      linear-gradient(180deg, rgba(255,255,255,0.35) 0%, rgba(255,255,255,0) 45%),
      linear-gradient(90deg, var(--photo-mid) 0%, var(--photo-light) 22%, var(--photo-warm) 50%, var(--photo-light) 78%, var(--photo-mid) 100%);
  }
  .cover__shapes {
    position: absolute;
    inset: 0;
    width: 982px;
    height: 362px;
  }

  .brand {
    position: absolute;
    display: flex;
    align-items: center;
  }
  .brand__mark {
    border-radius: 50%;
    background: var(--brand-orange-deep);
    flex: none;
  }
  .brand__name {
    font-family: "Montserrat", sans-serif;
    font-weight: 700;
    color: var(--text-light);
    letter-spacing: 2px;
    white-space: nowrap;
    line-height: 1;
  }
  .headline {
    position: absolute;
    font-family: "Montserrat", sans-serif;
    font-weight: 800;
    color: var(--text-light);
    white-space: nowrap;
    line-height: 1;
    text-align: center;
  }
  .body-copy {
    position: absolute;
    font-family: "Noto Sans", sans-serif;
    font-weight: 400;
    color: var(--text-light);
    font-size: 16px;
    line-height: 21.5px;
    white-space: nowrap;
  }

  /* centred layouts */
  .cover--orange-centre .brand,
  .cover--navy-centre .brand { left: 290px; top: 53px; }
  .cover--orange-centre .brand__mark,
  .cover--navy-centre .brand__mark { width: 83px; height: 83px; margin-right: 31px; }
  .cover--orange-centre .brand__name,
  .cover--navy-centre .brand__name { font-size: 31px; }
  .cover--orange-centre .headline,
  .cover--navy-centre .headline { left: 243px; width: 500px; top: 171px; font-size: 31px; }
  .cover--orange-centre .body-copy,
  .cover--navy-centre .body-copy { left: 274px; top: 234px; }

  /* right-hand layout */
  .cover--orange-right .brand { left: 554px; top: 68px; }
  .cover--orange-right .brand__mark { width: 76px; height: 76px; margin-right: 15px; }
  .cover--orange-right .brand__name { font-size: 28px; }
  .cover--orange-right .headline { left: 474px; width: 500px; top: 179px; font-size: 29px; }
  .cover--orange-right .body-copy { left: 523px; top: 243px; }
</style>
</head>
<body>
<main class="cover-set">

  <!-- Cover A: orange circle, centred -->
  <section class="cover cover--orange-centre">
    <div class="cover__photo" role="img" aria-label="Photo of smiling colleagues in a bright office meeting"></div>
    <svg class="cover__shapes" viewBox="0 0 1668 616" preserveAspectRatio="none" aria-hidden="true">
      <circle cx="837" cy="308" r="542" fill="var(--brand-navy)"/>
      <circle cx="842" cy="308" r="526" fill="var(--ring-white)"/>
      <circle cx="838" cy="308" r="510" fill="var(--brand-orange)"/>
    </svg>
    <div class="brand">
      <span class="brand__mark"></span>
      <span class="brand__name">CORVANE GROUP</span>
    </div>
    <h1 class="headline">#1 STAFFING COMPANY</h1>
    <p class="body-copy">Lorem ipsum dolor sit amet, consectetur adipiscing elit,<br>sed do eiusmod tempor incididunt ut labore et dolore<br>magna aliqua. Quis ipsum suspendisse ultrices gravida.</p>
  </section>

  <!-- Cover B: orange circle, right -->
  <section class="cover cover--orange-right">
    <div class="cover__photo" role="img" aria-label="Photo of a business team around a meeting table with laptop and charts"></div>
    <svg class="cover__shapes" viewBox="0 0 1668 616" preserveAspectRatio="none" aria-hidden="true">
      <circle cx="1280" cy="333" r="542" fill="var(--brand-navy)"/>
      <circle cx="1286" cy="333" r="528" fill="var(--ring-white)"/>
      <circle cx="1280" cy="333" r="512" fill="var(--brand-orange)"/>
      <rect x="1280" y="0" width="388" height="616" fill="var(--brand-orange)"/>
    </svg>
    <div class="brand">
      <span class="brand__mark"></span>
      <span class="brand__name">CORVANE GROUP</span>
    </div>
    <h2 class="headline">#1 STAFFING COMPANY</h2>
    <p class="body-copy">Lorem ipsum dolor sit amet, consectetur adipiscing<br>elit, sed do eiusmod tempor incididunt ut labore et<br>dolore magna aliqua. Quis ipsum suspendisse</p>
  </section>

  <!-- Cover C: navy circle, centred -->
  <section class="cover cover--navy-centre">
    <div class="cover__photo" role="img" aria-label="Photo of smiling colleagues in a bright office meeting"></div>
    <svg class="cover__shapes" viewBox="0 0 1668 616" preserveAspectRatio="none" aria-hidden="true">
      <circle cx="837" cy="308" r="542" fill="var(--brand-orange)"/>
      <circle cx="842" cy="308" r="526" fill="var(--ring-white)"/>
      <circle cx="838" cy="308" r="510" fill="var(--brand-navy-fill)"/>
    </svg>
    <div class="brand">
      <span class="brand__mark"></span>
      <span class="brand__name">CORVANE GROUP</span>
    </div>
    <h2 class="headline">#1 STAFFING COMPANY</h2>
    <p class="body-copy">Lorem ipsum dolor sit amet, consectetur adipiscing elit,<br>sed do eiusmod tempor incididunt ut labore et dolore<br>magna aliqua. Quis ipsum suspendisse ultrices gravida.</p>
  </section>

</main>
</body>
</html>
```